依頼詳細
平成26年     開業しましたが、平成27年1月より院の認知度アップ、新規患者様獲得の為
合計で2万枚程度を複数回に分けて新聞折込チラシを行います。
A4サイズでのチラシデザイン制作をお願いいたします。
現在制作中のホームページへの誘導を促したいのでURL入力のスペース確保や、『鈴風台接骨院で検索』などの記載をお願いします。
URLは12月12日現在決定していない為、仮のURLでのデザイン作成をお願いいたします。

シンプルながらも手に取った方の印象に残るような折込チラシデザインをお願いいたします。
記載項目
添付資料内のロゴ・HPサンプル等をご参照いただき、院名/住所/連絡先/受付時間/地図等の記載をお願いいたします。
サイズ
A4
ページ数
片面
希望イメージ
シンプル 複雑
単色 カラフル
暗い 明るい
日常 高級
遊び心 厳粛
未来的 伝統的
女性的 男性的
希望する色
納品ファイル
• 高解像度JPG (.jpg)
• イラストレーター形式 (.ai)
補足説明
ホームページURLはわかり次第ご連絡いたします。

この度はご提案いただきまして誠にありがとうございます。
納品までスムーズにご対応いただき、感謝いたします。
またの機会がございましたらよろしくお願いいたします。

納品までスムーズにご対応いただき、感謝いたします。

短い期間にもかかわらずたくさんのご提案いただき驚いております。

```html
<!DOCTYPE html>
<html lang="ja">
<head>
<meta charset="utf-8">
<title>鈴風台接骨院 チラシ</title>
<link rel="stylesheet" href="https://fonts.googleapis.com/css2?family=Noto+Sans+JP:wght@400;500;700&family=Noto+Serif+JP:wght@500;700&display=swap">
<style>
:root{
  --leaf-light:#e9f3c8;
  --leaf-mid:#b5d77a;
  --leaf-deep:#5f9a3a;
  --navy:#1d3f73;
  --brand:#2a6f95;
  --orange:#f08a24;
  --text:#333;
  --purple:#8e6fb8;
  --rose:#d86a8a;
  --amber:#e99a2c;
  --tangerine:#ef7e3c;
  --sky:#3f8fcf;
  --teal:#49ad9a;
  --red:#d8322a;
}
*{margin:0;padding:0;box-sizing:border-box}
html,body{width:849px;height:1200px;overflow:hidden;background:#fff}
body{font-family:"Noto Sans JP",sans-serif;color:var(--text);position:relative}
.leaves{position:absolute;background:radial-gradient(circle at 30% 30%,var(--leaf-light),var(--leaf-mid) 55%,var(--leaf-deep))}
.leaves--top{left:0;top:0;width:849px;height:398px}
.leaves--bottom{left:0;top:505px;width:849px;height:695px}
.greeting{position:absolute;left:440px;top:0;width:409px;height:398px;background:rgba(255,255,255,.93)}
.greeting__title{position:absolute;left:16px;top:12px;font-size:12px;font-weight:700;color:var(--navy)}
.greeting__body{position:absolute;left:16px;top:32px;width:240px;font-size:9.5px;line-height:1.55}
.greeting__photo{position:absolute;right:0;top:36px;width:150px;height:95px;background:linear-gradient(135deg,#e7ddd4,#c9b4a2)}
.symptoms{position:absolute;left:20px;top:212px;display:grid;grid-template-columns:repeat(3,80px);gap:8px 44px}
.symptom{width:80px;height:80px;border-radius:50%;color:#fff;font-size:9.5px;line-height:1.35;font-weight:500;display:flex;align-items:center;justify-content:center;text-align:center}
.s1{background:var(--purple)}.s2{background:var(--rose)}.s3{background:var(--amber)}
.s4{background:var(--tangerine)}.s5{background:var(--sky)}.s6{background:var(--teal)}
.masthead{position:absolute;left:0;top:398px;width:849px;height:107px;background:#fff;border-top:3px solid var(--navy);border-bottom:3px solid var(--navy)}
.masthead__tagline{position:absolute;left:430px;top:8px;font-family:"Noto Serif JP",serif;font-size:13px;letter-spacing:.3em;color:var(--navy)}
.masthead__name{position:absolute;left:0;width:100%;top:28px;text-align:center;font-family:"Noto Serif JP",serif;font-weight:700;font-size:56px;letter-spacing:.18em;color:var(--brand)}
.info{position:absolute;left:165px;top:515px;width:684px;height:685px;background:#fff}
.search-band{position:absolute;left:10px;top:12px;width:590px;height:22px;background:var(--orange);color:#fff;font-size:13px;font-weight:500;padding-left:12px;line-height:22px}
.url{position:absolute;left:10px;top:42px;font-size:23px;font-weight:500;color:var(--navy);letter-spacing:.02em}
.label{display:inline-block;background:var(--orange);color:#fff;font-size:10px;padding:1px 8px}
.contact{position:absolute;left:10px;top:80px}
.contact__lines{position:absolute;left:90px;top:0;font-size:12px;line-height:1.5;white-space:nowrap}
.hours{position:absolute;left:10px;top:130px;width:400px}
.hours table{margin-top:4px;border-collapse:collapse;font-size:11px;width:360px}
.hours th,.hours td{border-bottom:1px solid #bbb;padding:2px 4px;text-align:center}
.hours th:first-child,.hours td:first-child{text-align:left;width:130px}
.hours__notes{font-size:9px;line-height:1.5;margin-top:4px}
.map{position:absolute;left:10px;top:250px;width:370px;height:245px;background:linear-gradient(135deg,#eef2ee,#d9e3da);border:1px solid #c5cfc6}
.map__pin{position:absolute;left:150px;top:95px;background:#fff;border:1px solid var(--navy);font-size:11px;padding:2px 8px;color:var(--navy)}
.callout{position:absolute;left:610px;top:100px;writing-mode:vertical-rl;font-family:"Noto Serif JP",serif;font-size:22px;letter-spacing:.15em;color:var(--navy)}
.dot{position:absolute;border-radius:50%;opacity:.8}
.address{position:absolute;left:395px;top:470px;width:280px;text-align:right}
.address__main{font-size:13px;line-height:1.5;color:var(--navy);font-weight:500}
.address__sub{font-size:9px;line-height:1.6;margin-top:6px}
.address__parking{color:var(--red);font-weight:700;font-size:12px;margin-top:4px}
</style>
</head>
<body>
<div class="leaves leaves--top" role="img" aria-label="新緑の葉の写真"></div>

<section class="greeting">
  <h2 class="greeting__title">ごあいさつ</h2>
  <p class="greeting__body">鈴風台接骨院院長の森田です。<br>日常生活から交通事故、<br>スポーツ外傷まで幅広く<br>痛みでお困りの方の力になりたい。<br>そう考え地域に根ざした<br>治療を心がけております。<br>身体の不調は早めのご相談が大切です。<br>どうぞお気軽にご来院ください。<br>スタッフ一同お待ちしております。</p>
  <div class="greeting__photo" role="img" aria-label="施術風景の写真"></div>
  <div class="symptoms">
    <div class="symptom s1">ひざ痛<br>肘関節痛<br>腕のしびれ</div>
    <div class="symptom s2">首痛<br>肩こり<br>首のこわばり</div>
    <div class="symptom s3">骨盤<br>腰痛<br>臀部痛</div>
    <div class="symptom s4">ぎっくり腰<br>ヘルニアによる<br>痛み・しびれ</div>
    <div class="symptom s5">五十肩<br>野球肩<br>むちうち</div>
    <div class="symptom s6">テニス肘<br>野球肘<br>手のしびれ</div>
  </div>
</section>

<header class="masthead">
  <p class="masthead__tagline">痛みを癒し 人を助ける</p>
  <h1 class="masthead__name">鈴風台接骨院</h1>
</header>

<div class="leaves leaves--bottom" role="img" aria-label="新緑の葉の写真"></div>

<section class="info">
  <p class="search-band">ホームページ『鈴風台接骨院』で検索お願いします。</p>
  <p class="url">https://xxxx/xxxx/xxxx/xxxxxxxxxxxx</p>

  <div class="contact">
    <span class="label">お問い合わせ</span>
    <div class="contact__lines">tel:052-000-4418<br>mobile:090-0000-7312</div>
  </div>

  <div class="hours">
    <span class="label">受付時間</span>
    <table>
      <tr><th></th><th>月</th><th>火</th><th>水</th><th>木</th><th>金</th><th>土</th></tr>
      <tr><td>AM 8:30〜12:30</td><td>○</td><td>○</td><td>○</td><td>○</td><td>○</td><td>○</td></tr>
      <tr><td>PM 16:00〜20:00</td><td>○</td><td>○</td><td>○</td><td>○</td><td>○</td><td>－</td></tr>
    </table>
    <p class="hours__notes">上記時間以外も急患は受け付けております。<br>交通事故の治療は各種保険が適用されます。<br>初めての方は保険証をお持ちください。</p>
  </div>

  <div class="map" role="img" aria-label="周辺の案内地図">
    <span class="map__pin">鈴風台接骨院</span>
  </div>

  <p class="callout">痛みで困っていませんか？</p>
  <span class="dot" style="left:590px;top:90px;width:14px;height:14px;background:var(--amber)"></span>
  <span class="dot" style="left:650px;top:140px;width:10px;height:10px;background:var(--sky)"></span>
  <span class="dot" style="left:596px;top:300px;width:12px;height:12px;background:var(--rose)"></span>
  <span class="dot" style="left:655px;top:360px;width:16px;height:16px;background:var(--teal)"></span>
  <span class="dot" style="left:600px;top:410px;width:9px;height:9px;background:var(--purple)"></span>

  <div class="address">
    <p class="address__main">名古屋市緑区風見町3-8<br>サンプラザ風見1F</p>
    <p class="address__sub">地下鉄風見駅 2番出口より徒歩3分<br>市バス風見町停留所より徒歩1分<br>風見公園 西側すぐ</p>
    <p class="address__parking">駐車場有</p>
  </div>
</section>
</body>
</html>
```